Kobalto Cell Phone Repair

We are a small cell phone repair store in need of a redesign to our current business card to make it a more modern, cleaner design that will catch folks' attention (perhaps with rounded edges ) - But still include most of the information listed on the current card. Would like to keep the current color scheme of black/white and green. Card will not need any personnel name included. Would like to see some designs include takes on a velorin or tekvo screen as well as more traditional cards.

Target Market(s)

broad spectrum across all cell phone users

Industry/Entity Type

Cell Phone

Contact Information for Business Card

changes to front text:
keep business Logo
business address, phone number website and email. All other info optional (add gathernest and blurvo icons on card

Rear of card:

Keep repair services, change tekvo repair to slatra repair, change quorvex os repair to data recovery (with appropriate icon or substitute)
remove products text
remove pjw and ravesh from manufacturer logos, add dunbelio.

Requirements
Must have
• business Logo
• business address, phone number website and email
• keep colors to white/black/green/gray
• gathernest and blurvo icons on card
Nice to have
• Would like to see 'traditional' business card design as well as creative design incorporating incorporating front of cell phone (eg tekvo or quorvex). Rounded edges would be nice but not necessary.

```html
<!DOCTYPE html>
<html lang="en">
<head>
<meta charset="utf-8">
<title>Kobalto Cell Phone Repair – Business Card</title>
<link rel="stylesheet" href="https://fonts.googleapis.com/css2?family=Source+Sans+3:wght@400;600;700&family=Oswald:wght@600&display=swap">
<style>
  :root {
    --backdrop: #6f6f6f;
    --card: #ffffff;
    --ink: #111111;
    --green: #94c973;
    --brand-green: #4fae3a;
    --label-green: #6a8f5e;
    --rule: #c8c8c8;
    --divider: #6f8f62;
  }
  * { margin: 0; padding: 0; box-sizing: border-box; }
  html, body { width: 1200px; height: 900px; overflow: hidden; }
  body {
    background: var(--backdrop);
    position: relative;
    font-family: "Source Sans 3", "Myriad Pro", Arial, sans-serif;
    color: var(--ink);
  }
  .card {
    position: absolute;
    top: 271px;
    width: 457px;
    height: 282px;
    background: var(--card);
    border-radius: 14px;
    overflow: hidden;
    box-shadow: 5px 5px 6px rgba(0,0,0,0.45);
  }
  .card--front { left: 137px; }
  .card--back  { left: 626px; }

  /* Front */
  .logo {
    position: absolute;
    left: 128px; top: 20px;
    display: flex; align-items: center; gap: 12px;
  }
  .logo__mascot {
    width: 62px; height: 62px; border-radius: 50%;
    background: var(--brand-green);
  }
  .logo__name {
    font-family: "Oswald", "Source Sans 3", sans-serif;
    font-weight: 600;
    color: var(--ink);
    line-height: 0.95;
    text-transform: uppercase;
  }
  .logo__name .word { display: block; font-size: 46px; letter-spacing: -0.5px; }
  .logo__name .tag  { display: block; font-size: 15px; letter-spacing: 0.2px; margin-top: 2px; }

  .front__rule {
    position: absolute; left: 19px; right: 22px; top: 189px;
    border-top: 1px solid var(--rule);
  }
  .contact {
    position: absolute; left: 19px; top: 210px;
    font-size: 16px; line-height: 21px;
  }
  .contact b { font-weight: 700; }
  .social {
    position: absolute; right: 22px; top: 210px;
    font-size: 11px; color: #3a3a3a; font-weight: 600;
  }
  .address {
    position: absolute; right: 22px; top: 231px;
    font-size: 16px; line-height: 21px; text-align: right;
  }

  /* Back */
  .services__title {
    position: absolute; top: 20px; left: 0; right: 0;
    text-align: center; font-size: 22px; font-weight: 600;
    letter-spacing: 0.2px;
  }
  .services {
    position: absolute; top: 68px; left: 6px; right: 6px;
    display: flex; justify-content: space-around;
    list-style: none;
  }
  .service { width: 74px; text-align: center; }
  .service__photo {
    width: 62px; height: 62px; border-radius: 50%;
    margin: 0 auto 7px;
    border: 1px solid #9a9a9a;
  }
  .service__label {
    font-size: 15px; font-weight: 700; line-height: 17px;
    color: var(--label-green);
  }
  .photo--cracked  { background: radial-gradient(circle at 40% 40%, #6c7aa0, #2e3650); }
  .photo--water    { background: radial-gradient(circle at 50% 45%, #5f86b8, #c9dcef); }
  .photo--port     { background: linear-gradient(160deg, #2a2a2a, #8a8a8a 60%, #d6d6d6); }
  .photo--data     { background: radial-gradient(circle at 50% 50%, #d98a2e, #3c2a5c 70%); }
  .photo--unlock   { background: radial-gradient(circle at 50% 50%, #ffffff 30%, #3d63a6 75%); }
  .photo--tablet   { background: radial-gradient(circle at 50% 50%, #5a8ec4, #1d1d1d 72%); }

  .makers {
    position: absolute; left: 0; right: 0; top: 197px; height: 70px;
    background: var(--green);
    display: flex; align-items: center; justify-content: center;
    gap: 0;
  }
  .maker {
    font-size: 16px; font-weight: 700; color: var(--ink);
    padding: 0 12px; line-height: 30px;
    border-left: 1px solid var(--divider);
  }
  .maker:first-child { border-left: none; }
</style>
</head>
<body>

  <section class="card card--front" aria-label="Business card front">
    <div class="logo">
      <div class="logo__mascot" role="img" aria-label="Green lizard mascot waving and holding a phone"></div>
      <div class="logo__name">
        <span class="word">Kobalto</span>
        <span class="tag">Cell Phone Repair</span>
      </div>
    </div>

    <div class="front__rule"></div>

    <div class="contact">
      <p><b>P:</b> 410.555.0187</p>
      <p><b>E:</b> info@kobaltorepair.com</p>
      <p><b>W:</b> www.kobaltostore.com</p>
    </div>

    <p class="social">gathernest · blurvo</p>

    <div class="address">
      <p>1480 Harbor Row Ave,</p>
      <p>Calverton MD 21990</p>
    </div>
  </section>

  <section class="card card--back" aria-label="Business card back">
    <h2 class="services__title">CELL PHONE REPAIR SERVICE</h2>

    <ul class="services">
      <li class="service">
        <div class="service__photo photo--cracked" role="img" aria-label="Phone with a cracked screen"></div>
        <p class="service__label">Cracked screen</p>
      </li>
      <li class="service">
        <div class="service__photo photo--water" role="img" aria-label="Phone splashing into water"></div>
        <p class="service__label">Water Damage</p>
      </li>
      <li class="service">
        <div class="service__photo photo--port" role="img" aria-label="Close-up of a phone charging port"></div>
        <p class="service__label">Charging Port</p>
      </li>
      <li class="service">
        <div class="service__photo photo--data" role="img" aria-label="Phone with app icons spilling out"></div>
        <p class="service__label">Data Recovery</p>
      </li>
      <li class="service">
        <div class="service__photo photo--unlock" role="img" aria-label="Phone screen showing an open padlock"></div>
        <p class="service__label">Cell Phone Unlock</p>
      </li>
      <li class="service">
        <div class="service__photo photo--tablet" role="img" aria-label="Stack of tablets"></div>
        <p class="service__label">slatra Repair</p>
      </li>
    </ul>

    <div class="makers">
      <span class="maker">tekvo</span>
      <span class="maker">velorin</span>
      <span class="maker">Brambleo</span>
      <span class="maker">dunbelio</span>
      <span class="maker">Lunex</span>
    </div>
  </section>

</body>
</html>
```